Ridgeway Mortgage - Banner Ads for Re-Marketing Campaigns

Need a banner ad for a retargeting Campaign with Bright Tally.

We would like to incorporate our attached logo. Also would like to incorporate a call to action "Pre-Qualify for a home loan today" and a button to click. This banner is to encourage previous customers to come back to our website and submit information. It must look good on mobile and desktop.

Our website is RidgewayMortgage.com

Target Market(s)

Customers Seeking a Mortgage Loan

Industry/Entity Type

Mortgage

Requirements
Must have
• We would like the same basic design in the 4 sizes below.
• 728 pixels by 90 pixels leaderboard
• 300 by 250 medium rectangle
• 300 by 600 half page
• 320 by 100 mobile banner
Nice to have
• a Call to action, a button to click, animation
Should not have
• We are open.

```html
<!DOCTYPE html>
<html lang="en">
<head>
<meta charset="utf-8">
<title>Ridgeway Mortgage – Banner Set</title>
<link href="https://fonts.googleapis.com/css2?family=Cinzel:wght@400;500&family=Ubuntu:wght@700&family=Roboto+Condensed:wght@300&display=swap" rel="stylesheet">
<style>
  :root {
    --page: #ffffff;
    --sky-top: #f4f7fc;
    --sky-mid: #a9c6f0;
    --sky-deep: #5a8ee6;
    --grass: #7cc242;
    --grass-deep: #5aa32a;
    --brand-navy: #1f4f6e;
    --headline: #e6168c;
    --subline: #2c3e50;
    --button: #1c2530;
    --button-text: #ffffff;
    --logo-dot: #f4c20d;
    --label: #1f3b55;
    --hands-light: #f1cfb3;
    --hands-deep: #d9935b;
  }
  * { margin: 0; padding: 0; box-sizing: border-box; }
  html, body { width: 1200px; height: 1200px; overflow: hidden; background: var(--page); }
  .sheet { position: relative; width: 1200px; height: 1200px; }

  .banner { position: absolute; overflow: hidden; }
  .scene {
    position: absolute; inset: 0;
    background: linear-gradient(180deg, var(--sky-top) 0%, var(--sky-mid) 45%, var(--sky-deep) 78%, var(--grass) 80%, var(--grass-deep) 100%);
  }
  .hands-photo {
    position: absolute;
    border-radius: 40% 40% 48% 48%;
    background: radial-gradient(ellipse at 50% 40%, var(--hands-deep) 0%, var(--hands-light) 70%, rgba(241,207,179,0) 100%);
  }
  .brand { position: absolute; display: flex; align-items: center; }
  .brand-dot { border-radius: 50%; background: var(--logo-dot); flex: none; }
  .brand-name {
    font-family: "Cinzel", serif; font-weight: 400; color: var(--brand-navy);
    line-height: 1.05; letter-spacing: 0.02em;
  }
  .headline {
    position: absolute; font-family: "Ubuntu", sans-serif; font-weight: 700;
    color: var(--headline); white-space: nowrap; line-height: 1;
  }
  .subline {
    position: absolute; font-family: "Cinzel", serif; font-weight: 500;
    color: var(--subline); white-space: nowrap; line-height: 1;
  }
  .cta {
    position: absolute; background: var(--button); color: var(--button-text);
    border-radius: 999px; font-family: "Cinzel", serif; font-weight: 500;
    display: flex; align-items: center; justify-content: center;
    text-decoration: none; white-space: nowrap; letter-spacing: 0.04em;
  }
  .size-label {
    position: absolute; font-family: "Roboto Condensed", sans-serif; font-weight: 300;
    font-size: 30px; color: var(--label); transform: translateX(-50%); white-space: nowrap;
  }

  /* Leaderboard 728 x 90 */
  .leaderboard { left: 180px; top: 85px; width: 906px; height: 114px; }
  .leaderboard .brand { left: 60px; top: 36px; gap: 10px; }
  .leaderboard .brand-dot { width: 40px; height: 40px; }
  .leaderboard .brand-name { font-size: 22px; }
  .leaderboard .headline { left: 354px; top: 18px; font-size: 45px; }
  .leaderboard .subline { left: 398px; top: 66px; font-size: 17px; }
  .leaderboard .cta { left: 464px; top: 90px; width: 82px; height: 12px; font-size: 8px; }
  .leaderboard .hands-photo { left: 748px; top: 0; width: 150px; height: 110px; }

  /* Medium rectangle 300 x 250 */
  .rectangle { left: 166px; top: 339px; width: 359px; height: 299px; }
  .rectangle .brand { left: 20px; top: 49px; gap: 10px; }
  .rectangle .brand-dot { width: 52px; height: 52px; }
  .rectangle .brand-name { font-size: 19px; }
  .rectangle .hands-photo { left: 220px; top: 0; width: 139px; height: 109px; }
  .rectangle .headline { left: 146px; top: 131px; font-size: 32px; }
  .rectangle .subline { left: 162px; top: 170px; font-size: 13px; }
  .rectangle .cta { left: 213px; top: 187px; width: 79px; height: 11px; font-size: 7px; }

  /* Mobile banner */
  .mobile { left: 153px; top: 753px; width: 384px; height: 120px; }
  .mobile .brand { left: 31px; top: 8px; gap: 5px; }
  .mobile .brand-dot { width: 22px; height: 22px; }
  .mobile .brand-name { font-size: 10px; }
  .mobile .hands-photo { left: 276px; top: 0; width: 108px; height: 86px; }
  .mobile .headline { left: 115px; top: 36px; font-size: 26px; }
  .mobile .subline { left: 128px; top: 67px; font-size: 10px; }
  .mobile .cta { left: 173px; top: 81px; width: 38px; height: 6px; font-size: 4px; }

  /* Half page 300 x 600 */
  .half-page { left: 616px; top: 394px; width: 359px; height: 718px; }
  .half-page .scene {
    top: 246px;
    background: linear-gradient(180deg, var(--page) 0%, var(--sky-top) 18%, var(--sky-mid) 45%, var(--sky-deep) 82%, var(--grass) 84%, var(--grass-deep) 100%);
  }
  .half-page .hands-photo { left: 8px; top: 0; width: 344px; height: 246px; }
  .half-page .brand { left: 58px; top: 270px; gap: 14px; }
  .half-page .brand-dot { width: 60px; height: 60px; }
  .half-page .brand-name { font-size: 24px; }
  .half-page .headline { left: 48px; top: 338px; font-size: 48px; }
  .half-page .subline { left: 74px; top: 402px; font-size: 17.5px; }
  .half-page .cta { left: 147px; top: 430px; width: 80px; height: 12px; font-size: 8px; }
</style>
</head>
<body>
<main class="sheet">

  <section class="banner leaderboard">
    <div class="scene" role="img" aria-label="Photo of blue sky over a green meadow with a lone tree"></div>
    <div class="brand"><span class="brand-dot"></span><span class="brand-name">Ridgeway<br>Mortgage</span></div>
    <div class="headline">Pre-Quality</div>
    <div class="subline">FOR A HOME LOAN TODAY</div>
    <a class="cta" href="#">CLICK HERE</a>
    <div class="hands-photo" role="img" aria-label="Photo of cupped hands holding a small model house"></div>
  </section>
  <div class="size-label" style="left:548px; top:204px;">728 px X 90 px</div>

  <section class="banner rectangle">
    <div class="scene" role="img" aria-label="Photo of blue sky over a green meadow with a lone tree"></div>
    <div class="hands-photo" role="img" aria-label="Photo of cupped hands holding a small model house"></div>
    <div class="brand"><span class="brand-dot"></span><span class="brand-name">Ridgeway<br>Mortgage</span></div>
    <div class="headline">Pre-Quality</div>
    <div class="subline">FOR A HOME LOAN TODAY</div>
    <a class="cta" href="#">CLICK HERE</a>
  </section>
  <div class="size-label" style="left:352px; top:648px;">300 px X 250 px</div>

  <section class="banner mobile">
    <div class="scene" role="img" aria-label="Photo of blue sky over a green meadow with a lone tree"></div>
    <div class="brand"><span class="brand-dot"></span><span class="brand-name">Ridgeway<br>Mortgage</span></div>
    <div class="hands-photo" role="img" aria-label="Photo of cupped hands holding a small model house"></div>
    <div class="headline">Pre-Quality</div>
    <div class="subline">FOR A HOME LOAN TODAY</div>
    <a class="cta" href="#">CLICK HERE</a>
  </section>
  <div class="size-label" style="left:330px; top:882px;">300 px X 100 px</div>

  <section class="banner half-page">
    <div class="scene" role="img" aria-label="Photo of blue sky over a green meadow with a lone tree"></div>
    <div class="hands-photo" role="img" aria-label="Photo of cupped hands holding a small model house"></div>
    <div class="brand"><span class="brand-dot"></span><span class="brand-name">Ridgeway<br>Mortgage</span></div>
    <div class="headline">Pre-Quality</div>
    <div class="subline">FOR A HOME LOAN TODAY</div>
    <a class="cta" href="#">CLICK HERE</a>
  </section>
  <div class="size-label" style="left:780px; top:1120px;">300 px X 600 px</div>

</main>
</body>
</html>
```